Harbourline Rescue needs a one page colour brochure

We recently patent a new floating offshore lifeguard tower which has an attached high altitude blimp balloon. The blimp has camera attached high above the water which allow the lifeguard to see any sharks or people have gone under the water. I need a one page colour A4 size PDF brochure that I can email to potential clients. Its important that the headline and text are easy to read

Target Market(s)

Local Government & government officials that have responsibility for our beaches. Perhaps head lifeguard at a beach

Industry/Entity Type

Camera

Font styles to use
Sans Serif

Requirements
Must have
• 1. Most important clearly readable headline in large print
• 2. Next important detail clearly readable text outlining the benefit of the floating lifeguard tower.
• 3. Colour version of the lifeguard tower drawing.
• 4. The contact details and further information section can be in small but readable text.

```html
<!DOCTYPE html>
<html lang="en">
<head>
<meta charset="utf-8">
<title>Harbourline Rescue – Shark Watch Blimp Brochure</title>
<link rel="stylesheet" href="https://fonts.googleapis.com/css2?family=Ubuntu:wght@400;500;700&family=Open+Sans:ital,wght@0,400;0,600;0,700;1,400;1,600&display=swap">
<style>
  :root {
    --red: #e41e26;
    --blue: #2f62ad;
    --yellow: #f4ef86;
    --white: #ffffff;
    --grey-light: #f1f1f1;
    --grey-mid: #c9c9c9;
    --ink: #1d1d1d;
    --footer-bg: #f2f2f3;
    --icon-blue: #2f5ea8;
    --sky-top: #2b7ac6;
    --sky-bottom: #a9d2ef;
    --sea: #35b6e8;
  }
  * { box-sizing: border-box; margin: 0; padding: 0; }
  html, body { width: 960px; height: 1200px; overflow: hidden; background: var(--white); }
  .brochure { position: relative; width: 960px; height: 1200px; overflow: hidden; font-family: "Open Sans", Arial, sans-serif; color: var(--ink); }

  .masthead { position: absolute; top: 0; left: 0; width: 960px; height: 221px; background: var(--red); text-align: center; color: var(--white); }
  .masthead__title { font-family: "Ubuntu", Arial, sans-serif; font-weight: 700; font-size: 45px; letter-spacing: -0.5px; padding-top: 38px; text-shadow: 2px 3px 6px rgba(0,0,0,0.35); }
  .masthead__subtitle { font-family: "Ubuntu", Arial, sans-serif; font-weight: 400; font-size: 32px; line-height: 44px; margin-top: 10px; text-shadow: 1px 2px 5px rgba(0,0,0,0.3); }

  .stripe { position: absolute; left: 0; width: 960px; height: 13px; background: var(--yellow); }
  .stripe--top { top: 221px; }
  .stripe--bottom { top: 851px; }

  .feature-panel { position: absolute; top: 234px; left: 0; width: 960px; height: 617px; background: var(--blue); }

  .illustration-frame { position: absolute; top: 205px; left: 23px; width: 505px; height: 678px; background: var(--white); padding: 11px; box-shadow: 3px 4px 10px rgba(0,0,0,0.35); z-index: 2; }
  .illustration { width: 100%; height: 100%; background: linear-gradient(180deg, var(--sky-top) 0%, var(--sky-bottom) 68%, var(--sea) 72%, #1f9fd9 100%); }

  .benefits { position: absolute; top: 294px; left: 557px; width: 380px; list-style: none; color: var(--white); z-index: 2; }
  .benefits__item { position: relative; padding-left: 26px; font-style: italic; font-size: 16px; line-height: 22px; margin-bottom: 14px; }
  .benefits__item--small { font-size: 15px; line-height: 20.5px; margin-bottom: 16px; }
  .benefits__tick { position: absolute; left: 0; top: 3px; width: 17px; height: 17px; }

  .product-band { position: absolute; top: 864px; left: 0; width: 960px; height: 150px; background: linear-gradient(180deg, var(--white) 0%, var(--grey-light) 55%, var(--grey-mid) 100%); text-align: center; }
  .product-band__name { font-family: "Ubuntu", Arial, sans-serif; font-weight: 400; font-size: 34px; line-height: 44px; padding-top: 30px; color: var(--ink); text-shadow: 1px 2px 4px rgba(0,0,0,0.25); }

  .reassurance { position: absolute; top: 1015px; left: 0; width: 960px; height: 77px; background: var(--red); color: var(--white); text-align: center; font-family: "Open Sans", Arial, sans-serif; font-size: 25px; letter-spacing: 1.8px; line-height: 31px; padding-top: 8px; }

  .contact-bar { position: absolute; top: 1092px; left: 0; width: 960px; height: 108px; background: var(--footer-bg); display: flex; align-items: center; }
  .contact-bar__brand { width: 165px; padding-left: 22px; font-family: "Open Sans", Arial, sans-serif; font-weight: 700; font-size: 18px; line-height: 20px; color: var(--icon-blue); }
  .contact-item { display: flex; align-items: center; font-style: italic; font-size: 12.5px; line-height: 16px; color: var(--ink); }
  .contact-item__icon { width: 34px; height: 34px; flex: none; margin-right: 9px; }
  .contact-item--post { margin-left: 37px; width: 235px; }
  .contact-item--phone { width: 255px; }
  .contact-item--mail { width: 250px; }
</style>
</head>
<body>
<main class="brochure">
  <header class="masthead">
    <h1 class="masthead__title">ANNOUNCING THE WATER IS SHARK SAFE</h1>
    <p class="masthead__subtitle">With Our New High Altitude Shark Watch Blimp<br>And Floating Offshore Lifeguard Tower</p>
  </header>

  <div class="stripe stripe--top"></div>
  <section class="feature-panel"></section>
  <div class="stripe stripe--bottom"></div>

  <figure class="illustration-frame">
    <div class="illustration" role="img" aria-label="Coloured drawing of a tethered camera blimp flying above a red floating lifeguard watch tower standing in the sea, with a shark swimming beneath the waves"></div>
  </figure>

  <ul class="benefits">
    <li class="benefits__item"><svg class="benefits__tick" viewBox="0 0 20 20"><circle cx="10" cy="10" r="10" fill="#fff"/><path d="M5 10.5l3.2 3.2L15 7" fill="none" stroke="#2f62ad" stroke-width="2.6" stroke-linecap="round" stroke-linejoin="round"/></svg>Can see sharks or swimmers several metres underwater</li>
    <li class="benefits__item"><svg class="benefits__tick" viewBox="0 0 20 20"><circle cx="10" cy="10" r="10" fill="#fff"/><path d="M5 10.5l3.2 3.2L15 7" fill="none" stroke="#2f62ad" stroke-width="2.6" stroke-linecap="round" stroke-linejoin="round"/></svg>Is significantly cheaper to operate than a helicopter or aerial drone</li>
    <li class="benefits__item"><svg class="benefits__tick" viewBox="0 0 20 20"><circle cx="10" cy="10" r="10" fill="#fff"/><path d="M5 10.5l3.2 3.2L15 7" fill="none" stroke="#2f62ad" stroke-width="2.6" stroke-linecap="round" stroke-linejoin="round"/></svg>Can provides 24 hours a day high altitude surveillance, not just a once a day fly over</li>
    <li class="benefits__item"><svg class="benefits__tick" viewBox="0 0 20 20"><circle cx="10" cy="10" r="10" fill="#fff"/><path d="M5 10.5l3.2 3.2L15 7" fill="none" stroke="#2f62ad" stroke-width="2.6" stroke-linecap="round" stroke-linejoin="round"/></svg>Only requires one person to operate, no need for a pilot and observer</li>
    <li class="benefits__item benefits__item--small"><svg class="benefits__tick" viewBox="0 0 20 20"><circle cx="10" cy="10" r="10" fill="#fff"/><path d="M5 10.5l3.2 3.2L15 7" fill="none" stroke="#2f62ad" stroke-width="2.6" stroke-linecap="round" stroke-linejoin="round"/></svg>Our floating lifeguard tower also provides a shorter rescue distance than land based towers</li>
    <li class="benefits__item benefits__item--small"><svg class="benefits__tick" viewBox="0 0 20 20"><circle cx="10" cy="10" r="10" fill="#fff"/><path d="M5 10.5l3.2 3.2L15 7" fill="none" stroke="#2f62ad" stroke-width="2.6" stroke-linecap="round" stroke-linejoin="round"/></svg>Simple assembled and disassembly for winter storage, easily moved to different beach locations</li>
    <li class="benefits__item benefits__item--small"><svg class="benefits__tick" viewBox="0 0 20 20"><circle cx="10" cy="10" r="10" fill="#fff"/><path d="M5 10.5l3.2 3.2L15 7" fill="none" stroke="#2f62ad" stroke-width="2.6" stroke-linecap="round" stroke-linejoin="round"/></svg>Our floating Lifeguard tower is designed like an offshore oil platform for all weather conditions, stormy rough seas and hurricane winds</li>
    <li class="benefits__item benefits__item--small"><svg class="benefits__tick" viewBox="0 0 20 20"><circle cx="10" cy="10" r="10" fill="#fff"/><path d="M5 10.5l3.2 3.2L15 7" fill="none" stroke="#2f62ad" stroke-width="2.6" stroke-linecap="round" stroke-linejoin="round"/></svg>Patent Pending</li>
  </ul>

  <section class="product-band">
    <h2 class="product-band__name">Harbourline Rescue’s Two In One High Altitude Blimp<br>And Floating Lifeguard Watch Tower</h2>
  </section>

  <p class="reassurance">Finally, our eye in the sky shark blimp provides reassurance<br>to tourist and swimmers that it’s safe to swim</p>

  <footer class="contact-bar">
    <div class="contact-bar__brand">Harbourline Rescue</div>
    <div class="contact-item contact-item--post">
      <svg class="contact-item__icon" viewBox="0 0 34 34"><circle cx="17" cy="17" r="17" fill="#2f5ea8"/><path d="M17 8a6 6 0 0 0-6 6c0 4.5 6 12 6 12s6-7.5 6-12a6 6 0 0 0-6-6z" fill="#fff"/><circle cx="17" cy="14" r="2.3" fill="#2f5ea8"/></svg>
      <span>PO Box 512, Rosehill<br>NSW 2142, Australia</span>
    </div>
    <div class="contact-item contact-item--phone">
      <svg class="contact-item__icon" viewBox="0 0 34 34"><circle cx="17" cy="17" r="17" fill="#2f5ea8"/><path d="M12.5 9.5l3 3-1.8 2.2c.9 2 2.6 3.7 4.6 4.6l2.2-1.8 3 3-2 2.4c-5.5-.6-10.6-5.7-11.2-11.2z" fill="#fff"/></svg>
      <span>Local: (02) 5550 1234<br>International: +61 2 5550 1234</span>
    </div>
    <div class="contact-item contact-item--mail">
      <svg class="contact-item__icon" viewBox="0 0 34 34"><circle cx="17" cy="17" r="17" fill="#2f5ea8"/><rect x="9" y="11.5" width="16" height="11" rx="1" fill="#fff"/><path d="M9.5 12.5L17 18l7.5-5.5" fill="none" stroke="#2f5ea8" stroke-width="1.4"/></svg>
      <span>Cal Whitmore<br>cal@harbourlinerescue.example</span>
    </div>
  </footer>
</main>
</body>
</html>
```